Business Card Design Project

I need a cool business card design for the company that will build residential houses.
The card should include:
1) Name: Borek Valdisov
2) Cell: 587.244.XXXX
3) Email: bor.valdisov@qorvina.example
4) Position: General Manager
5) Residential Home Building
6) Company logo that I have uploaded

Industry/Entity Type

Residential

```html
<!DOCTYPE html>
<html lang="en">
<head>
<meta charset="utf-8">
<title>Borek Valdisov — Business Card</title>
<link rel="stylesheet" href="https://fonts.googleapis.com/css2?family=PT+Sans&family=Tinos&display=swap">
<style>
  :root {
    --card-bg: #c9ebc6;
    --house-green: #77d96b;
    --band-grey: #86b08e;
    --logo-panel: #e0f2e6;
    --contact-ink: #4a6a50;
    --name-ink: #eaf8e8;
    --title-ink: #555b57;
    --brand-ink: #3d7fc4;
  }
  html, body {
    margin: 0;
    padding: 0;
    overflow: hidden;
    background: var(--card-bg);
  }
  .card {
    position: relative;
    width: 1200px;
    height: 687px;
    background: var(--card-bg);
    overflow: hidden;
    font-family: "PT Sans", sans-serif;
  }
  .card-art {
    position: absolute;
    inset: 0;
  }
  .brand-panel {
    position: absolute;
    left: 871px;
    top: 13px;
    width: 329px;
    height: 144px;
    background: var(--logo-panel);
    display: flex;
    align-items: center;
    justify-content: flex-end;
    gap: 10px;
    padding-right: 22px;
    box-sizing: border-box;
  }
  .brand-mark {
    width: 22px;
    height: 22px;
    background: var(--brand-ink);
  }
  .brand-name {
    font-family: "PT Sans", sans-serif;
    font-size: 26px;
    color: var(--brand-ink);
    line-height: 1;
  }
  .contact {
    position: absolute;
    left: 407px;
    top: 437px;
    color: var(--contact-ink);
    font-size: 28px;
    line-height: 31px;
    letter-spacing: -0.3px;
  }
  .contact p { margin: 0; }
  .person-name {
    position: absolute;
    right: 11px;
    top: 513px;
    margin: 0;
    font-family: "Tinos", serif;
    font-weight: 400;
    font-size: 51px;
    line-height: 60px;
    letter-spacing: -2.5px;
    color: var(--name-ink);
  }
  .person-title {
    position: absolute;
    right: 13px;
    top: 576px;
    margin: 0;
    font-family: "Tinos", serif;
    font-size: 26px;
    line-height: 34px;
    color: var(--title-ink);
  }
</style>
</head>
<body>
  <main class="card">
    <svg class="card-art" width="1200" height="687" viewBox="0 0 1200 687" aria-hidden="true">
      <polygon class="house" points="0,306 198,198 402,306 402,506 0,506" fill="var(--house-green)"/>
      <rect class="chimney" x="402" y="0" width="59" height="306" fill="var(--house-green)"/>
      <rect class="name-band" x="0" y="506" width="1200" height="68" fill="var(--house-green)"/>
      <rect class="title-band" x="0" y="574" width="1200" height="40" fill="var(--band-grey)"/>
    </svg>

    <div class="brand-panel">
      <span class="brand-mark"></span>
      <span class="brand-name">Qorvina Developments</span>
    </div>

    <div class="contact">
      <p class="contact-phone">587.244.XXXX</p>
      <p class="contact-email">bor.valdisov@qorvina.example</p>
    </div>

    <h1 class="person-name">Borek Valdisov</h1>
    <p class="person-title">General Manager</p>
  </main>
</body>
</html>
```